Business Card Design Project

Thornwick Property Management

Our Business is residential property management, we therefore need a card that displays a professional image, but is clear and concise, and easy to read
Updates

We are committed now guys and girls, loving what we are seeing so far! 

Target Market(s)

Landlords, Rental Property Owners

Industry/Entity Type

Residential

Requirements
Must have
• Dale Thornwick - Principal
Fiona Thornwick - Director (Property Management)

PO Box 817
Pellworth SA 5193

Dale: 0490 367 258
Fiona: 0490 723 519

www.thornwickpropertymanagement.com.au
admin@thornwickpropertymanagement.com.au

Nice to have
• I would like the card to be double sided, white background on the information side and then colour on the reverse, in blue or black and incorporating our logo

```html
<!DOCTYPE html>
<html lang="en">
<head>
<meta charset="utf-8">
<title>Thornwick Property Management – Business Card</title>
<link rel="stylesheet" href="https://fonts.googleapis.com/css2?family=Arimo:wght@400;700&display=swap">
<style>
  :root {
    --backdrop: #e4e6e9;
    --card: #ffffff;
    --brand-blue: #1f6fb5;
    --ink: #3a3b3d;
    --ink-soft: #555759;
    --swoosh-dark: #1b1c1e;
    --rule: #c9ccd0;
  }
  * { margin: 0; padding: 0; box-sizing: border-box; }
  html, body { width: 1200px; height: 951px; overflow: hidden; }
  body {
    background: var(--backdrop);
    font-family: "Arimo", Arial, sans-serif;
    color: var(--ink);
    position: relative;
  }
  .card {
    position: absolute;
    width: 660px;
    height: 380px;
    background: var(--card);
    border-radius: 26px;
    overflow: hidden;
    box-shadow: 0 6px 18px rgba(0,0,0,0.18);
  }
  .card--front { left: 60px; top: 60px; }
  .card--back { left: 480px; top: 510px; }

  .wordmark { display: flex; align-items: center; gap: 14px; }
  .wordmark__square { width: 60px; height: 60px; background: var(--brand-blue); flex: none; }
  .wordmark__name {
    font-weight: 700;
    color: var(--ink);
    line-height: 1.05;
    white-space: nowrap;
  }
  .card--front .wordmark { position: absolute; left: 78px; top: 120px; }
  .card--front .wordmark__name { font-size: 40px; }
  .front__web {
    position: absolute; left: 0; right: 0; top: 270px;
    text-align: center; font-size: 19px; color: #222;
  }

  .swoosh { position: absolute; inset: 0; }
  .people {
    position: absolute; left: 30px; top: 66px; width: 228px;
    text-align: right;
  }
  .people__name { color: var(--brand-blue); font-size: 21px; line-height: 1.1; white-space: nowrap; }
  .people__role { color: var(--ink-soft); font-size: 15px; line-height: 1.2; margin-bottom: 6px; white-space: nowrap; }
  .divider {
    position: absolute; left: 274px; top: 66px; width: 1px; height: 124px;
    background: var(--rule);
  }
  .contact {
    position: absolute; left: 288px; top: 64px; width: 330px; list-style: none;
    font-size: 14px; color: var(--ink);
  }
  .contact__item { display: flex; align-items: flex-start; gap: 7px; line-height: 19px; white-space: nowrap; }
  .contact__item--gap { margin-bottom: 16px; }
  .contact__icon { width: 14px; height: 14px; flex: none; margin-top: 2px; fill: var(--brand-blue); }
  .card--back .wordmark { position: absolute; left: 48px; top: 268px; }
  .card--back .wordmark__square { width: 48px; height: 48px; }
  .card--back .wordmark__name { font-size: 30px; }
</style>
</head>
<body>

<section class="card card--front" aria-label="Card front">
  <div class="wordmark">
    <span class="wordmark__square"></span>
    <span class="wordmark__name">Thornwick<br>Property Management</span>
  </div>
  <p class="front__web">www.thornwickpropertymanagement.com.au</p>
</section>

<section class="card card--back" aria-label="Card back">
  <svg class="swoosh" viewBox="0 0 660 380" preserveAspectRatio="none" aria-hidden="true">
    <path d="M0 0 H115 Q30 40 0 150 Z" fill="var(--brand-blue)"/>
    <path d="M0 160 Q28 48 130 0 H142 Q44 50 0 175 Z" fill="var(--swoosh-dark)"/>
    <path d="M660 380 H545 Q630 340 660 230 Z" fill="var(--brand-blue)"/>
    <path d="M660 220 Q632 332 530 380 H518 Q616 330 660 205 Z" fill="var(--swoosh-dark)"/>
  </svg>

  <div class="people">
    <p class="people__name">Dale Thornwick</p>
    <p class="people__role">Principal</p>
    <p class="people__name">Fiona Thornwick</p>
    <p class="people__role">Director<br>(Property Management)</p>
  </div>

  <div class="divider"></div>

  <ul class="contact">
    <li class="contact__item contact__item--gap">
      <svg class="contact__icon" viewBox="0 0 16 16"><path d="M8 1 L15 8 H13 V15 H10 V10 H6 V15 H3 V8 H1 Z"/></svg>
      <span>PO Box 817<br>Pellworth SA 5193</span>
    </li>
    <li class="contact__item">
      <svg class="contact__icon" viewBox="0 0 16 16"><path d="M4 1 L7 4 L5 6 Q7 10 10 11 L12 9 L15 12 L12 15 Q2 13 1 4 Z"/></svg>
      <span>Dale: 0490 367 258</span>
    </li>
    <li class="contact__item">
      <svg class="contact__icon" viewBox="0 0 16 16"><path d="M4 1 L7 4 L5 6 Q7 10 10 11 L12 9 L15 12 L12 15 Q2 13 1 4 Z"/></svg>
      <span>Fiona: 0490 723 519</span>
    </li>
    <li class="contact__item">
      <svg class="contact__icon" viewBox="0 0 16 16"><circle cx="8" cy="8" r="7"/></svg>
      <span>www.thornwickpropertymanagement.com.au</span>
    </li>
    <li class="contact__item">
      <svg class="contact__icon" viewBox="0 0 16 16"><path d="M1 3 H15 V13 H1 Z M2 4 L8 9 L14 4" fill="none" stroke="var(--brand-blue)" stroke-width="2"/></svg>
      <span>admin@thornwickpropertymanagement.com.au</span>
    </li>
  </ul>

  <div class="wordmark">
    <span class="wordmark__square"></span>
    <span class="wordmark__name">Thornwick<br>Property Management</span>
  </div>
</section>

</body>
</html>
```